Uregent Care opening postcard with coupon

We need a postcard created to mail directly to homes. The flyer need to be appealing and include a small spot with a coupon for $20 gift card with first visit. The post card needs to be 2 sided and 4X6. We have a logo. To learn more about us visit northglenclinicplus.com or check us out on facebook. I will try to figure out how to upload logo.

Target Market(s)

All households that need urgent care.

Industry/Entity Type

Healthcare

Font styles to use
Serif

Colors
33a6d7
447fba
85acd3
85cae6
cfdfed
ecf7fb

Requirements
Must have
• our logo
• family centered
• some services offered
• coupon with free $20 gc at first visit if you bring in this flyer
Nice to have
• visually appealing

```html
<!DOCTYPE html>
<html lang="en">
<head>
<meta charset="utf-8">
<title>Northglen Clinic Plus – Postcard</title>
<link rel="stylesheet" href="https://fonts.googleapis.com/css2?family=Open+Sans:wght@400;600;700;800&family=Roboto+Condensed:wght@400;500;700&display=swap">
<style>
  :root{
    --sky:#33a6d7;
    --mid-blue:#447fba;
    --soft-blue:#85acd3;
    --light-sky:#85cae6;
    --mist:#cfdfed;
    --ice:#ecf7fb;
    --navy:#23286b;
    --royal:#3a4ea0;
    --deep:#2a5d98;
    --lime:#9cc43a;
    --lime-dark:#6f9a1f;
    --page:#e9ecef;
    --white:#ffffff;
  }
  *{box-sizing:border-box;margin:0;padding:0}
  html,body{width:815px;height:1200px;overflow:hidden}
  body{background:var(--page);font-family:"Open Sans",Arial,sans-serif;position:relative}

  .postcard{position:absolute;left:96px;width:622px;height:481px;background:var(--white);overflow:hidden;box-shadow:0 6px 14px rgba(0,0,0,.25)}
  .postcard--front{top:80px}
  .postcard--back{top:636px}

  .shape-layer{position:absolute;left:0;top:0}

  .footer-band{position:absolute;left:0;bottom:0;width:100%;height:61px;background:linear-gradient(90deg,var(--sky),var(--mid-blue) 70%,var(--deep));color:var(--white);font-weight:700;font-size:12.6px;display:flex;align-items:center;padding:0 30px 0 14px;white-space:nowrap}
  .footer-band .sep{margin:0 6px}

  .brand{position:absolute;display:flex;align-items:center;gap:10px}
  .brand-mark{width:26px;height:26px;background:var(--navy)}
  .brand-name{font-family:"Roboto Condensed",Arial,sans-serif;font-weight:700;color:var(--navy);font-size:25px;line-height:1.02;text-transform:uppercase}
  .postcard--front .brand{left:378px;top:36px}
  .postcard--back .brand{left:30px;top:30px}

  .gift-card{position:absolute;background:linear-gradient(160deg,#f4f6f8,#dfe3e8);border:1px solid #c9ced4;box-shadow:0 3px 6px rgba(0,0,0,.25);font-family:"Roboto Condensed",Arial,sans-serif;font-weight:500;color:var(--royal);text-transform:uppercase;display:flex;flex-direction:column;justify-content:center}
  .postcard--front .gift-card{left:378px;top:106px;width:219px;height:112px;padding-left:16px;font-size:21px;line-height:1.28}
  .postcard--back .gift-card{left:17px;top:316px;width:177px;height:89px;padding-left:13px;font-size:17px;line-height:1.3}

  .services{position:absolute;left:396px;top:240px;width:210px;color:var(--royal)}
  .services-title{font-size:10.6px;font-weight:800;line-height:1.5;text-transform:uppercase;margin-bottom:8px}
  .services-list{list-style:none;font-size:12.2px;line-height:16.3px}
  .services-list li{position:relative;padding-left:19px}
  .services-list li::before{content:"";position:absolute;left:2px;top:5px;width:7px;height:7px;border-radius:50%;background:var(--soft-blue)}

  .badge{position:absolute;width:94px;height:94px;border-radius:50%;background:radial-gradient(circle at 40% 35%,#b7da54,var(--lime) 60%,var(--lime-dark));color:var(--white);font-weight:700;font-size:10.4px;line-height:1.2;text-align:center;text-transform:uppercase;display:flex;align-items:center;justify-content:center;box-shadow:0 2px 4px rgba(0,0,0,.25)}
  .postcard--front .badge{left:22px;top:340px}
  .postcard--back .badge{left:290px;top:224px}

  .family-band{position:absolute;left:0;top:261px;width:366px;height:37px;background:var(--royal);color:var(--white);font-weight:700;font-size:14.5px;display:flex;align-items:center;justify-content:center;padding-right:18px;text-transform:uppercase}
  .coupon-panel{position:absolute;left:0;top:298px;width:360px;height:122px;background:linear-gradient(90deg,var(--mid-blue),#4f8cc6)}
  .hours{position:absolute;left:213px;top:310px;color:var(--white);font-size:9.6px;line-height:13px;font-weight:700}
  .hours-title{text-transform:uppercase;margin-bottom:1px}

  .stamp-box{position:absolute;left:522px;top:28px;width:80px;height:53px;border:1.5px solid #c8ccd1}
  .address-line{position:absolute;left:392px;width:210px;height:0;border-top:1.5px solid #c8ccd1}
</style>
</head>
<body>

<!-- Front -->
<section class="postcard postcard--front">
  <svg class="shape-layer" width="622" height="481" viewBox="0 0 622 481">
    <defs>
      <linearGradient id="frontBase" x1="0" y1="0" x2="1" y2="1">
        <stop offset="0" stop-color="#eef0ea"/>
        <stop offset=".55" stop-color="#d7c6bc"/>
        <stop offset="1" stop-color="#a9574c"/>
      </linearGradient>
      <radialGradient id="frontWarmRight" cx="0.72" cy="0.55" r="0.45">
        <stop offset="0" stop-color="#d24c3e" stop-opacity=".85"/>
        <stop offset="1" stop-color="#d24c3e" stop-opacity="0"/>
      </radialGradient>
      <radialGradient id="frontPinkLeft" cx="0.15" cy="0.62" r="0.4">
        <stop offset="0" stop-color="#d99ab8" stop-opacity=".8"/>
        <stop offset="1" stop-color="#d99ab8" stop-opacity="0"/>
      </radialGradient>
      <radialGradient id="frontLight" cx="0.7" cy="0.1" r="0.4">
        <stop offset="0" stop-color="#ffffff" stop-opacity=".9"/>
        <stop offset="1" stop-color="#ffffff" stop-opacity="0"/>
      </radialGradient>
      <radialGradient id="frontSkin" cx="0.55" cy="0.28" r="0.25">
        <stop offset="0" stop-color="#c98f72" stop-opacity=".7"/>
        <stop offset="1" stop-color="#c98f72" stop-opacity="0"/>
      </radialGradient>
    </defs>
    <path d="M330 0 H354 Q392 210 366 420 H346 Q372 210 330 0 Z" fill="var(--light-sky)"/>
    <g role="img" aria-label="Photo of a nurse taking an older man's blood pressure at home">
      <path d="M0 0 H330 Q372 210 346 420 H0 Z" fill="url(#frontBase)"/>
      <path d="M0 0 H330 Q372 210 346 420 H0 Z" fill="url(#frontLight)"/>
      <path d="M0 0 H330 Q372 210 346 420 H0 Z" fill="url(#frontSkin)"/>
      <path d="M0 0 H330 Q372 210 346 420 H0 Z" fill="url(#frontPinkLeft)"/>
      <path d="M0 0 H330 Q372 210 346 420 H0 Z" fill="url(#frontWarmRight)"/>
    </g>
  </svg>

  <div class="brand">
    <span class="brand-mark"></span>
    <span class="brand-name">Northglen<br>Clinic Plus</span>
  </div>

  <div class="gift-card"><span>$20 Gift Card</span><span>With First Visit</span></div>

  <div class="services">
    <p class="services-title">We are here for your<br>everyday healthcare needs</p>
    <ul class="services-list">
      <li>Urgent Care</li>
      <li>Medication Refills</li>
      <li>Lab Tests &amp; Vaccinations</li>
      <li>Well Exams</li>
      <li>Health Screenings</li>
      <li>Pediatrics</li>
      <li>Infections</li>
      <li>Preventive Services</li>
    </ul>
  </div>

  <div class="badge">No<br>Appointments<br>Needed!</div>

  <div class="footer-band">WWW.NORTHGLENCLINICPLUS.COM<span class="sep">|</span>2140 HARBOR LANE MILLBROOK<span class="sep">|</span>(555) 214-0398</div>
</section>

<!-- Back -->
<section class="postcard postcard--back">
  <svg class="shape-layer" width="622" height="481" viewBox="0 0 622 481">
    <defs>
      <linearGradient id="backBase" x1="0" y1="0" x2="0" y2="1">
        <stop offset="0" stop-color="#5f7a3c"/>
        <stop offset=".55" stop-color="#8e9a7a"/>
        <stop offset="1" stop-color="#93a6bb"/>
      </linearGradient>
      <radialGradient id="backWarm" cx="0.5" cy="0.5" r="0.35">
        <stop offset="0" stop-color="#c99878" stop-opacity=".85"/>
        <stop offset="1" stop-color="#c99878" stop-opacity="0"/>
      </radialGradient>
      <radialGradient id="backCool" cx="0.3" cy="0.95" r="0.4">
        <stop offset="0" stop-color="#a9bdd3" stop-opacity=".9"/>
        <stop offset="1" stop-color="#a9bdd3" stop-opacity="0"/>
      </radialGradient>
      <radialGradient id="backLeaf" cx="0.9" cy="0.15" r="0.35">
        <stop offset="0" stop-color="#3f5a2a" stop-opacity=".8"/>
        <stop offset="1" stop-color="#3f5a2a" stop-opacity="0"/>
      </radialGradient>
    </defs>
    <path d="M330 0 H352 Q382 210 352 420 H336 Q366 210 330 0 Z" fill="var(--light-sky)"/>
    <g role="img" aria-label="Photo of a smiling family of five outdoors">
      <path d="M0 94 H356 Q366 180 362 261 H0 Z" fill="url(#backBase)"/>
      <path d="M0 94 H356 Q366 180 362 261 H0 Z" fill="url(#backLeaf)"/>
      <path d="M0 94 H356 Q366 180 362 261 H0 Z" fill="url(#backCool)"/>
      <path d="M0 94 H356 Q366 180 362 261 H0 Z" fill="url(#backWarm)"/>
    </g>
  </svg>

  <div class="brand">
    <span class="brand-mark"></span>
    <span class="brand-name">Northglen<br>Clinic Plus</span>
  </div>

  <div class="family-band">Family Centered</div>
  <div class="coupon-panel"></div>

  <div class="gift-card"><span>$20 Gift Card</span><span>With First Visit</span></div>

  <div class="hours">
    <p class="hours-title">Operating Hours</p>
    <p>Monday 7a-7p</p>
    <p>Tuesday 7a-7p</p>
    <p>Wednesday 7a-7p</p>
    <p>Thursday 7a-7p</p>
    <p>Friday 7a-7p</p>
    <p>Saturday 7a-7p</p>
    <p>Sunday 10a-7p</p>
  </div>

  <div class="badge">No<br>Appointments<br>Needed!</div>

  <div class="stamp-box"></div>
  <div class="address-line" style="top:190px"></div>
  <div class="address-line" style="top:222px"></div>
  <div class="address-line" style="top:254px"></div>
  <div class="address-line" style="top:286px"></div>

  <div class="footer-band">WWW.NORTHGLENCLINICPLUS.COM<span class="sep">|</span>2140 HARBOR LANE MILLBROOK<span class="sep">|</span>(555) 214-0398</div>
</section>

</body>
</html>
```